BANNER FOR ONLINE CABINET COMPANY MAIN PAGE

Need 3 different banners for the main page. We are online platform for ordering cabinets, parts etc. online.
Website: bordaline.ca
A place where the banner will be placed: https://view.pelmoraclip.com/qTR7WkVbNHEa4
Banner size: 1344x399 pixels
****Clients should get the main point that they can order everything online through the website.

Industry/Entity Type

online cabinets and parts ordering

Requirements
Must have
• online ordering icons, vexaphone, laptop, desktop pc - so clients get an idea that this is web based service to order cabinets

```html
<!DOCTYPE html>
<html lang="en">
<head>
<meta charset="utf-8">
<title>Bordaline banner</title>
<link href="https://fonts.googleapis.com/css2?family=Roboto:wght@400;700&family=Archivo+Black&display=swap" rel="stylesheet">
<style>
  :root {
    --page-bg: #f2f2f2;
    --rose: #e8adad;
    --rose-line: #d99aa3;
    --charcoal: #33363a;
    --white: #ffffff;
    --photo-light: #ece9e4;
    --photo-warm: #d8c2a4;
    --accent: #e0503f;
  }
  html, body {
    margin: 0;
    width: 1200px;
    height: 545px;
    overflow: hidden;
    background: var(--page-bg);
  }
  .banner {
    position: absolute;
    left: 0;
    top: 95px;
    width: 1200px;
    height: 356px;
    overflow: hidden;
    background: var(--rose);
  }
  .banner-art {
    position: absolute;
    inset: 0;
  }
  .brand {
    position: absolute;
    left: 62px;
    top: 44px;
    display: flex;
    align-items: center;
    gap: 12px;
    font-family: "Roboto", sans-serif;
    font-weight: 700;
    font-size: 50px;
    line-height: 60px;
    color: var(--white);
    letter-spacing: -0.5px;
  }
  .brand-mark {
    width: 22px;
    height: 22px;
    border-radius: 50%;
    background: var(--accent);
  }
  .categories {
    position: absolute;
    left: 58px;
    top: 140px;
    margin: 0;
    padding: 0;
    list-style: none;
    font-family: "Roboto", sans-serif;
    font-weight: 400;
    font-size: 31px;
    line-height: 48.5px;
    color: var(--white);
  }
  .device-icons {
    position: absolute;
    left: 455px;
    top: 178px;
    width: 230px;
    height: 110px;
  }
  .order-button {
    position: absolute;
    left: 905px;
    top: 268px;
    width: 160px;
    height: 30px;
    border-radius: 15px;
    background: var(--white);
    display: flex;
    align-items: center;
    justify-content: center;
    font-family: "Archivo Black", sans-serif;
    font-size: 16px;
    letter-spacing: 1.5px;
    color: var(--charcoal);
  }
  .site-url {
    position: absolute;
    left: 885px;
    width: 200px;
    top: 305px;
    text-align: center;
    font-family: "Roboto", sans-serif;
    font-size: 18px;
    color: var(--white);
  }
</style>
</head>
<body>
  <section class="banner">
    <svg class="banner-art" width="1200" height="356" viewBox="0 0 1200 356">
      <defs>
        <linearGradient id="kitchenTone" x1="0" y1="0" x2="1" y2="0">
          <stop offset="0" stop-color="#e7a9a9"/>
          <stop offset="1" stop-color="#eab4b3"/>
        </linearGradient>
        <linearGradient id="shelfTone" x1="0" y1="0" x2="0" y2="1">
          <stop offset="0" stop-color="var(--photo-warm)"/>
          <stop offset="0.35" stop-color="var(--photo-light)"/>
          <stop offset="1" stop-color="#f4f3f1"/>
        </linearGradient>
      </defs>
      <rect width="1200" height="356" fill="url(#kitchenTone)" role="img" aria-label="Pink-tinted photo of a kitchen with range hood, open shelves and countertop"/>
      <polygon points="0,241 0,356 125,356" fill="var(--charcoal)"/>
      <polygon points="700,170 844,27 874,37 909,0 1200,0 1200,356 870,356"
               fill="url(#shelfTone)" role="img" aria-label="Photo of white kitchen shelves with jars, cups and utensils over a tiled wall"/>
      <line x1="875" y1="0" x2="1040" y2="165" stroke="var(--rose-line)" stroke-width="3"/>
      <line x1="1170" y1="150" x2="1010" y2="310" stroke="var(--rose-line)" stroke-width="3"/>
      <line x1="1110" y1="0" x2="1200" y2="90" stroke="var(--rose-line)" stroke-width="3"/>
      <polygon points="841,314 985,170 1166,356 884,356" fill="var(--charcoal)"/>
    </svg>

    <div class="brand"><span>Bordaline</span><span class="brand-mark"></span></div>

    <ul class="categories">
      <li>DECORATIVE HARDWARE</li>
      <li>KITCHEN ACCESSORIES</li>
      <li>VANITIES</li>
    </ul>

    <svg class="device-icons" viewBox="0 0 230 110" role="img" aria-label="Desktop, laptop and phone icons for online ordering">
      <g fill="none" stroke="var(--white)" stroke-width="3.5" stroke-linejoin="round" stroke-linecap="round">
        <!-- desktop -->
        <rect x="4" y="8" width="86" height="60" rx="4"/>
        <line x1="47" y1="68" x2="47" y2="86"/>
        <line x1="28" y1="88" x2="66" y2="88"/>
        <!-- laptop -->
        <rect x="110" y="34" width="64" height="42" rx="3"/>
        <path d="M100 84 H184 L180 92 H104 Z"/>
        <!-- phone -->
        <rect x="196" y="48" width="28" height="50" rx="4"/>
        <line x1="206" y1="90" x2="214" y2="90"/>
      </g>
      <circle cx="47" cy="38" r="6" fill="var(--accent)"/>
      <circle cx="142" cy="55" r="5" fill="var(--accent)"/>
    </svg>

    <div class="order-button">ORDER NOW</div>
    <div class="site-url">www.bordaline.ca</div>
  </section>
</body>
</html>
```